PRESENTATION FOLDER DESIGN

I would like to design a presentation folder that is 6 x 9 with 2 x 4 inch pockets.
I have attached the logo to use as well as the template for the presentation folder.

I also included the front and back of the business cards so that you can see the overall look I am trying to go for as well as the information to have on there.

The presentation folder will be used to send out an invitation to a conference for dentists.

Target Market(s)

dentists

Font styles to use
Sans Serif

Requirements
Must have
• The clours must be the same as on the logo.
• On the cover, I would like a title in bold large letters that says:
• PLEASE JOIN US FOR OUR EXCLUSIVE EVENTS
• FOR DENTAL PROFESSIONALS
• *eligible for CE credits
• I would like to have this picture on the cover as well.
• ON THE BACK, i WOULD THE COLOURS TO BE THE BLUE FROM THE LOGO AND THE WRITING IN WHITE.
• THE INSIDE FLAPS MUST BE IN THE BLUE BUT THE INSIDE OF THE FOLDER SHOULD BE IN ORANGE.
• ON THE INSIDE FLAPS WE SHOULD WRITE:
• ON THE LEFT FLAP: I WANT TO PURCHASE A CLINIC
• ON THE RIGHT FLAP: I WANT TO SELL MY CLINIC

```html
<!DOCTYPE html>
<html lang="en">
<head>
<meta charset="UTF-8">
<title>Presentation Folder – Inside Spread</title>
<link href="https://fonts.googleapis.com/css2?family=Montserrat:wght@500;700&display=swap" rel="stylesheet">
<style>
  :root {
    --stage: #e4e4e4;
    --orange: #df5a1f;
    --orange-light: #e8692c;
    --orange-deep: #cf4f18;
    --blue: #33b8d4;
    --blue-deep: #2aa7c2;
    --white: #ffffff;
  }
  * { box-sizing: border-box; margin: 0; padding: 0; }
  html, body {
    width: 1200px;
    height: 850px;
    overflow: hidden;
    background: var(--stage);
    font-family: "Montserrat", sans-serif;
  }
  .folder-spread {
    position: absolute;
    left: 80px;
    top: 35px;
    width: 1040px;
    height: 780px;
    display: flex;
  }
  .folder-panel {
    position: relative;
    width: 520px;
    height: 780px;
    overflow: hidden;
  }
  .panel-surface {
    position: absolute;
    inset: 0;
    background: linear-gradient(160deg, var(--orange-light) 0%, var(--orange) 45%, var(--orange-deep) 100%);
  }
  .folder-panel--left .panel-surface { box-shadow: inset -6px 0 10px rgba(0,0,0,0.12); }
  .folder-panel--right .panel-surface { box-shadow: inset 6px 0 10px rgba(0,0,0,0.12); }
  .pocket {
    position: absolute;
    left: 0;
    bottom: 0;
    width: 520px;
    height: 270px;
  }
  .pocket svg {
    position: absolute;
    inset: 0;
    width: 100%;
    height: 100%;
  }
  .pocket-label {
    position: absolute;
    left: 0;
    right: 0;
    top: 95px;
    display: flex;
    flex-direction: column;
    align-items: center;
    color: var(--white);
    line-height: 1;
  }
  .pocket-label__lead {
    font-weight: 500;
    font-size: 22px;
    letter-spacing: 1px;
    margin-left: -20px;
  }
  .pocket-label__action {
    font-weight: 700;
    font-size: 66px;
    letter-spacing: 1px;
    margin: 6px 0 4px -16px;
  }
  .pocket-label__tail {
    font-weight: 500;
    font-size: 24px;
    letter-spacing: 1px;
    margin-left: 24px;
  }
</style>
</head>
<body>
  <main class="folder-spread">
    <section class="folder-panel folder-panel--left">
      <div class="panel-surface" role="img" aria-label="Orange inner panel with a faint repeating brand-mark pattern"></div>
      <div class="pocket">
        <svg viewBox="0 0 520 270" preserveAspectRatio="none" aria-hidden="true">
          <path d="M0 90 Q240 45 520 28 L520 270 L0 270 Z" fill="var(--blue)"/>
          <path d="M0 90 Q240 45 520 28" fill="none" stroke="var(--blue-deep)" stroke-width="3"/>
        </svg>
        <div class="pocket-label">
          <span class="pocket-label__lead">I WANT TO</span>
          <span class="pocket-label__action">BUY</span>
          <span class="pocket-label__tail">A CLINIC</span>
        </div>
      </div>
    </section>
    <section class="folder-panel folder-panel--right">
      <div class="panel-surface" role="img" aria-label="Orange inner panel with a faint repeating brand-mark pattern"></div>
      <div class="pocket">
        <svg viewBox="0 0 520 270" preserveAspectRatio="none" aria-hidden="true">
          <path d="M0 40 Q250 20 520 0 L520 270 L0 270 Z" fill="var(--blue)"/>
          <path d="M0 40 Q250 20 520 0" fill="none" stroke="var(--blue-deep)" stroke-width="3"/>
        </svg>
        <div class="pocket-label">
          <span class="pocket-label__lead">I WANT TO</span>
          <span class="pocket-label__action">SELL</span>
          <span class="pocket-label__tail">A CLINIC</span>
        </div>
      </div>
    </section>
  </main>
</body>
</html>
```